GPS Tracker Business Card Design

We need a business card for a GPS Vehicle tracking company. We sell the hardware for the vehicle and the software platform to monitor your vehicle/s. Including high asset non-powered vehicles like a trailer using our solar powered unit.
We like using dark blue to different shades of blue along with gold. We have phone apps for Android and Apple devices.

We have a platform for families wanting to track their teenage driver and children; Plus a Fleet vehicle tracking platform.

Features: unlimited number of vehicles and/or assets including snow mobiles forklifts generators trailers airport equipment

Reports for driving behavior reports and alerts dashboard fleet maintenace timeline view and replay geofence real time alerts logbook scheduling route optimization accounting integration fleet grouping closest vehicle locator On Board Diagnostics.

Benefits: Increased productivity improved fuel efficiency organizing your business improve time management simplify back end processes, reduce fleet fuel efficiency and expenses increase fleet security etc..

Please view website: Velmorix.com

Industry/Entity Type

Business

Contact Information for Business Card

Harold P Simkins

```html
<!DOCTYPE html>
<html lang="en">
<head>
<meta charset="utf-8">
<title>Velmorix Business Card</title>
<link rel="stylesheet" href="https://fonts.googleapis.com/css2?family=Raleway:wght@300&family=Arimo:wght@400;700&display=swap">
<style>
  :root {
    --page-bg: #e9e6e1;
    --card-navy: #0f1f5c;
    --card-navy-deep: #0a1646;
    --card-edge: #07103a;
    --accent-blue: #2a7fd4;
    --text-light: #e8eef8;
    --badge-black: #111111;
    --icon-blue: #1f6fc4;
    --globe-light: #5cc4f0;
    --globe-deep: #1c3ea8;
  }
  * { box-sizing: border-box; margin: 0; padding: 0; }
  html, body { width: 1200px; height: 780px; overflow: hidden; }
  body {
    background: var(--page-bg);
    font-family: "Arimo", Arial, sans-serif;
    position: relative;
  }
  .card {
    position: absolute;
    width: 560px;
    height: 320px;
    border-radius: 4px;
    background: linear-gradient(135deg, var(--card-navy) 0%, var(--card-navy-deep) 100%);
    box-shadow: 0 3px 0 var(--card-edge), 0 6px 0 var(--card-edge), 0 14px 24px rgba(0,0,0,0.25);
    overflow: hidden;
    color: var(--text-light);
  }
  .card-front { left: 60px; top: 60px; }
  .card-back { left: 580px; top: 400px; }

  .wordmark {
    font-family: "Raleway", Arial, sans-serif;
    font-weight: 300;
    color: var(--text-light);
    letter-spacing: 1px;
    line-height: 1;
  }

  /* Front */
  .front-brand { position: absolute; left: 34px; top: 44px; }
  .front-brand .wordmark { font-size: 44px; }
  .phone-badge {
    display: inline-block;
    margin-top: 12px;
    background: var(--badge-black);
    color: #ffffff;
    font-weight: 700;
    font-size: 15px;
    padding: 2px 6px;
  }
  .holder { position: absolute; left: 34px; top: 168px; }
  .holder-name { font-size: 22px; }
  .holder-title { font-size: 15px; color: var(--accent-blue); margin-top: 2px; }
  .contact-list { position: absolute; left: 34px; top: 232px; list-style: none; }
  .contact-list li { display: flex; align-items: center; gap: 8px; font-size: 15px; height: 24px; }
  .contact-icon { width: 16px; height: 16px; background: var(--icon-blue); border-radius: 2px; display: flex; align-items: center; justify-content: center; }
  .globe-art {
    position: absolute; right: -6px; top: -30px; width: 260px; height: 260px; border-radius: 50%;
    background: radial-gradient(circle at 35% 35%, var(--globe-light) 0%, #2a78d0 45%, var(--globe-deep) 80%, transparent 81%);
  }
  .social-row { position: absolute; right: 26px; bottom: 26px; display: flex; gap: 8px; }
  .social-square { width: 24px; height: 24px; background: var(--icon-blue); border-radius: 2px; }

  /* Back */
  .back-photo {
    position: absolute; inset: 0;
    background: radial-gradient(ellipse at 70% 45%, rgba(70,100,180,0.35) 0%, rgba(15,31,92,0) 65%);
  }
  .back-brand { position: absolute; right: 40px; top: 40px; }
  .back-brand .wordmark { font-size: 72px; }
  .benefits { position: absolute; left: 34px; right: 34px; top: 178px; }
  .benefits-heading { font-size: 20px; color: var(--accent-blue); margin-bottom: 10px; }
  .benefits-text { font-size: 15px; line-height: 1.45; color: var(--text-light); }
</style>
</head>
<body>

<section class="card card-front">
  <div class="globe-art" role="img" aria-label="Glowing blue globe with arrows circling it"></div>

  <div class="front-brand">
    <div class="wordmark">Velmorix</div>
    <div class="phone-badge">555-210-4476</div>
  </div>

  <div class="holder">
    <div class="holder-name">Harold P Simkins</div>
    <div class="holder-title">Owner</div>
  </div>

  <ul class="contact-list">
    <li>
      <span class="contact-icon">
        <svg width="10" height="10" viewBox="0 0 10 10"><path d="M2 1 L4 1 L4.6 3 L3.6 3.8 Q4.6 5.6 6.2 6.4 L7 5.4 L9 6 L9 8 Q5 9 1 2 Z" fill="#fff"/></svg>
      </span>555-210-4476
    </li>
    <li>
      <span class="contact-icon">
        <svg width="10" height="10" viewBox="0 0 10 10"><rect x="1" y="2" width="8" height="6" fill="none" stroke="#fff"/><path d="M1 2 L5 5.5 L9 2" fill="none" stroke="#fff"/></svg>
      </span>harold@velmorix.com
    </li>
    <li>
      <span class="contact-icon">
        <svg width="10" height="10" viewBox="0 0 10 10"><circle cx="5" cy="5" r="4" fill="none" stroke="#fff"/><path d="M1 5 H9 M5 1 V9" stroke="#fff" fill="none"/></svg>
      </span>www.velmorix.com
    </li>
  </ul>

  <div class="social-row">
    <span class="social-square"></span>
    <span class="social-square"></span>
    <span class="social-square"></span>
  </div>
</section>

<section class="card card-back">
  <div class="back-photo" role="img" aria-label="Faint photo of hands on a keyboard with a world map overlay"></div>

  <div class="back-brand">
    <div class="wordmark">Velmorix</div>
  </div>

  <div class="benefits">
    <div class="benefits-heading">Benefits</div>
    <p class="benefits-text">Increased productivity improved fuel efficiency organizing your business improve time management simplify back end processes, reduce fleet fuel efficiency and expenses increase fleet security etc.</p>
  </div>
</section>

</body>
</html>
```